web page look and feel - B2B enterprise application

We have an enterprise application with 10 to 15 core pages and several supporting pages or popups. To start, we want the graphical design of the Users, Roles and Data Source pages and their supporting popups, wizards, etc. to be made beautiful. That is around 10 pages in total. There is a fair amount of redundancy among the pages. I have attached 5 screenshots. We very much want the pages to project a premium feel. That is absolutely essential. The color scheme is blue and sometimes yellow (only if it makes the page look better) plus black, gray and white. If the design of these screens goes well, we would expand the project to continue with other pages. The core of what we are looking for is graphic in nature but we are open to workflow suggestions if you have them. The Roles screen needs some improvements to the layout. I am looking for everything that includes icons, fonts, spacing, etc. I assume getting to the final design will take some back and forth with multiple revisions.

Target Market(s)

Large Enterprises

Number of Pages Required

5+ page

Requirements
Must have
• Premium feel

```html
<!DOCTYPE html>
<html lang="en">
<head>
<meta charset="utf-8">
<title>Users – Kestrel Data</title>
<link href="https://fonts.googleapis.com/css2?family=Roboto:wght@400;500;700&display=swap" rel="stylesheet">
<style>
:root{
  --sidebar:#1f2338;
  --sidebar-band:#343b5c;
  --header:#363d63;
  --accent:#2f6db5;
  --accent-dark:#285f9e;
  --page:#e9eaee;
  --card:#ffffff;
  --line:#9a9da8;
  --line-soft:#d4d6dc;
  --grey-row:#f1f1f3;
  --text:#2a2c33;
  --btn-dark:#474a52;
  --white:#ffffff;
}
*{box-sizing:border-box;margin:0;padding:0}
html,body{width:1200px;height:1021px;overflow:hidden}
body{font-family:'Roboto',sans-serif;background:var(--page);color:var(--text);position:relative}
.sidebar{position:absolute;left:0;top:0;width:214px;height:1021px;background:var(--sidebar);color:var(--white)}
.brand{height:76px;display:flex;align-items:center;padding-left:30px;gap:10px;font-size:23px;font-weight:500;letter-spacing:-.3px}
.brand-dot{width:14px;height:14px;border-radius:50%;background:#f0b429}
.nav-band{position:absolute;left:0;width:214px;background:var(--sidebar-band);display:flex;align-items:center;font-size:13.5px}
.nav-band .ico{width:53px;height:100%;display:flex;align-items:center;justify-content:center;background:rgba(0,0,0,.12)}
.nav-band .label{padding-left:10px}
.nav-band.active{background:var(--accent)}
.nav-band.active .ico{background:var(--accent-dark)}
.nav-sub{position:absolute;font-size:13px;color:var(--white)}
.topbar{position:absolute;left:214px;top:0;width:986px;height:76px;background:var(--header)}
.burger{position:absolute;left:33px;top:29px}
.top-icons{position:absolute;left:624px;top:26px;display:flex;gap:17px}
.avatar{position:absolute;left:783px;top:18px;width:40px;height:40px;border-radius:50%;background:radial-gradient(circle at 50% 40%,#c89a7c,#5a4538)}
.user-name{position:absolute;left:832px;top:30px;color:var(--white);font-size:14px;font-weight:500;display:flex;align-items:center;gap:5px}
.page-title{position:absolute;left:260px;top:106px;font-size:26px;font-weight:400;color:#2d2f37}
.btn-add{position:absolute;left:334px;top:111px;width:52px;height:26px;background:var(--header);color:var(--white);font-size:15px;display:flex;align-items:center;justify-content:center;border-radius:2px}
.search{position:absolute;left:968px;top:100px;width:200px;height:31px;display:flex}
.search-input{flex:1;background:var(--white);border:1px solid #cfd1d6;font-size:11px;color:#555;padding:9px 7px}
.search-btn{width:30px;background:var(--accent);display:flex;align-items:center;justify-content:center}
.card{position:absolute;left:251px;top:159px;width:911px;height:729px;background:var(--card);border:1px solid #e0e1e5}
.users-table{position:absolute;left:19px;top:21px;width:872px;height:652px;border:1px solid #b9c7dc;border-top:none}
.row{display:grid;grid-template-columns:40px 124px 135px 137px 158px 103px 175px;align-items:stretch;border-bottom:1px solid var(--line)}
.row>div{display:flex;align-items:center;justify-content:center;font-size:12.5px;border-left:1px solid var(--line)}
.row>div:first-child{border-left:none}
.row.head{height:48px;background:linear-gradient(#3d446c,#30375a);color:var(--white);border-bottom:none}
.row.head>div{font-size:13.5px;font-weight:500;gap:4px;border-left:1px solid #4c5478}
.row.head>div:first-child{border-left:none}
.row.open{height:48px}
.row.item{height:51px}
.actions{gap:4px}
.act{width:26px;height:26px;border-radius:3px;background:var(--btn-dark);display:flex;align-items:center;justify-content:center}
.act.del{background:var(--accent)}
.detail{height:272px;border-bottom:1px solid var(--line);padding:32px 22px 0 22px}
.perm{width:828px;border:1px solid var(--line-soft)}
.perm-row{display:grid;grid-template-columns:427px 401px;height:41px;border-bottom:1px solid var(--line-soft);font-size:14px}
.perm-row:last-child{border-bottom:none}
.perm-row>div{display:flex;align-items:center}
.perm-row>div:first-child{padding-left:15px;border-right:1px solid var(--line-soft)}
.perm-row>div:last-child{padding-left:83px;gap:22px}
.perm-row.shaded{background:var(--grey-row)}
.check{display:flex;align-items:center;gap:6px}
.box{width:12px;height:12px;border-radius:2px;background:var(--header);display:flex;align-items:center;justify-content:center}
.pager{position:absolute;left:20px;top:689px;display:flex;gap:8px}
.pg{height:22px;min-width:22px;padding:0 5px;border:1px solid #d9dbe0;background:#f7f7f9;font-size:10px;display:flex;align-items:center;justify-content:center;color:#333}
.pg.wide{width:44px}
.pg.current{background:var(--header);color:var(--white);border-color:var(--header)}
.footer{position:absolute;left:588px;top:972px;font-size:10px;color:#333}
</style>
</head>
<body>
<aside class="sidebar">
  <div class="brand"><span class="brand-dot"></span>Kestrel Data</div>
  <div class="nav-band active" style="top:76px;height:44px"><div class="ico"><svg width="14" height="15" viewBox="0 0 14 15"><circle cx="7" cy="4" r="3.5" fill="#fff"/><path d="M0 15c0-5 3-7 7-7s7 2 7 7z" fill="#fff"/></svg></div><span class="label">Users</span></div>
  <div class="nav-sub" style="left:66px;top:138px">Roles</div>
  <div class="nav-sub" style="left:66px;top:170px">Notification Groups</div>
  <div class="nav-band" style="top:203px;height:44px"><div class="ico"><svg width="15" height="15" viewBox="0 0 16 16"><circle cx="8" cy="8" r="5" fill="none" stroke="#fff" stroke-width="3" stroke-dasharray="3 1.6"/><circle cx="8" cy="8" r="2" fill="#fff"/></svg></div><span class="label">Data Sources</span></div>
  <div class="nav-sub" style="left:62px;top:265px">Data Object Relationships</div>
  <div class="nav-band" style="top:297px;height:45px"><div class="ico"><svg width="13" height="16" viewBox="0 0 13 16"><path d="M0 0h8l5 5v11H0z" fill="#fff"/><path d="M3 8h7M3 11h7" stroke="#343b5c" stroke-width="1.2"/></svg></div><span class="label">Data Sets</span></div>
  <div class="nav-band" style="top:342px;height:44px;border-top:1px solid #2a3050"><div class="ico"><svg width="15" height="15" viewBox="0 0 16 16"><path d="M8 1l7 3v8l-7 3-7-3V4z" fill="#fff"/><path d="M1 4l7 3 7-3M8 7v8" stroke="#343b5c" stroke-width="1.2" fill="none"/></svg></div><span class="label">Rule Sets</span></div>
  <div class="nav-band" style="top:386px;height:45px;border-top:1px solid #2a3050"><div class="ico"><svg width="16" height="15" viewBox="0 0 16 15"><rect x="1" y="3" width="11" height="11" fill="none" stroke="#fff" stroke-width="1.5"/><path d="M6 10l1-3 7-7 2 2-7 7z" fill="#fff"/></svg></div><span class="label">Schedules</span></div>
  <div class="nav-band" style="top:431px;height:45px;border-top:1px solid #2a3050"><div class="ico"><svg width="13" height="16" viewBox="0 0 13 16"><path d="M0 0h8l5 5v11H0z" fill="#fff"/><path d="M3 8h7M3 11h7" stroke="#343b5c" stroke-width="1.2"/></svg></div><span class="label">Metadata Import/Export</span></div>
  <div class="nav-sub" style="left:65px;top:490px">Import</div>
  <div class="nav-sub" style="left:65px;top:522px">Export</div>
</aside>

<header class="topbar">
  <svg class="burger" width="19" height="16" viewBox="0 0 19 16"><path d="M0 1.5h19M0 8h19M0 14.5h19" stroke="#fff" stroke-width="2.4"/></svg>
  <div class="top-icons">
    <svg width="24" height="22" viewBox="0 0 24 22"><path d="M2 17a10 10 0 1 1 20 0z" fill="#fff"/><path d="M12 16l5-8" stroke="#363d63" stroke-width="2"/><circle cx="12" cy="16" r="2" fill="#363d63"/></svg>
    <svg width="22" height="22" viewBox="0 0 22 22"><path d="M2 20L15 7" stroke="#fff" stroke-width="3"/><path d="M17 1l1 3 3 1-3 1-1 3-1-3-3-1 3-1z" fill="#fff"/></svg>
    <svg width="22" height="22" viewBox="0 0 22 22"><circle cx="11" cy="11" r="10" fill="#fff"/><path d="M8 8.5a3 3 0 1 1 4 2.8c-1 .4-1 1-1 2.2" stroke="#363d63" stroke-width="2.2" fill="none"/><circle cx="11" cy="16.5" r="1.3" fill="#363d63"/></svg>
    <svg width="22" height="22" viewBox="0 0 22 22"><circle cx="11" cy="11" r="7" fill="none" stroke="#fff" stroke-width="5" stroke-dasharray="3.5 2"/><circle cx="11" cy="11" r="6" fill="#fff"/><circle cx="11" cy="11" r="2.5" fill="#363d63"/></svg>
  </div>
  <div class="avatar" role="img" aria-label="User profile photo"></div>
  <div class="user-name">Mara Linwood <svg width="9" height="6" viewBox="0 0 9 6"><path d="M1 1l3.5 3.5L8 1" stroke="#fff" stroke-width="1.5" fill="none"/></svg></div>
</header>

<h1 class="page-title">Users</h1>
<div class="btn-add">ADD</div>
<div class="search"><div class="search-input">Search</div><div class="search-btn"><svg width="16" height="16" viewBox="0 0 16 16"><circle cx="6.5" cy="6.5" r="5" fill="none" stroke="#fff" stroke-width="2.2"/><path d="M10 10l5 5" stroke="#fff" stroke-width="2.4"/></svg></div></div>

<main class="card">
  <div class="users-table">
    <div class="row head">
      <div></div>
      <div>First Name <svg width="8" height="5"><path d="M0 0h8L4 5z" fill="#fff"/></svg></div>
      <div>Last Name <svg width="8" height="5"><path d="M0 0h8L4 5z" fill="#fff"/></svg></div>
      <div>Username <svg width="8" height="5"><path d="M0 0h8L4 5z" fill="#fff"/></svg></div>
      <div>Email Address <svg width="8" height="5"><path d="M0 0h8L4 5z" fill="#fff"/></svg></div>
      <div>Status <svg width="8" height="5"><path d="M0 0h8L4 5z" fill="#fff"/></svg></div>
      <div></div>
    </div>
    <div class="row open">
      <div><svg width="11" height="7" viewBox="0 0 11 7"><path d="M1 1l4.5 4.5L10 1" stroke="#363d63" stroke-width="2" fill="none"/></svg></div>
      <div>tim</div><div>tim</div><div>tim.timtim</div><div>tim@kestreldata.net</div><div>Active</div>
      <div class="actions"><span class="act"><svg width="12" height="12" viewBox="0 0 12 12"><path d="M1 11l1-3 6-6 2 2-6 6z" fill="#fff"/></svg></span><span class="act"><svg width="12" height="12" viewBox="0 0 12 12"><rect x="3" y="1" width="8" height="8" fill="#fff"/><path d="M1 3v8h8" stroke="#fff" stroke-width="1.4" fill="none"/></svg></span><span class="act del"><svg width="11" height="12" viewBox="0 0 11 12"><path d="M0 2h11M4 0h3" stroke="#fff" stroke-width="1.4"/><path d="M1.5 3h8l-.7 9H2.2z" fill="#fff"/></svg></span></div>
    </div>
    <div class="detail">
      <div class="perm">
        <div class="perm-row shaded"><div>Object</div><div>Permissions</div></div>
        <div class="perm-row"><div>System Settings</div><div><span class="check"><span class="box"><svg width="8" height="6"><path d="M1 3l2 2 4-4" stroke="#fff" stroke-width="1.5" fill="none"/></svg></span>Read</span><span class="check"><span class="box"><svg width="8" height="6"><path d="M1 3l2 2 4-4" stroke="#fff" stroke-width="1.5" fill="none"/></svg></span>Write</span></div></div>
        <div class="perm-row"><div>Users</div><div><span class="check"><span class="box"><svg width="8" height="6"><path d="M1 3l2 2 4-4" stroke="#fff" stroke-width="1.5" fill="none"/></svg></span>Read</span><span class="check"><span class="box"><svg width="8" height="6"><path d="M1 3l2 2 4-4" stroke="#fff" stroke-width="1.5" fill="none"/></svg></span>Write</span></div></div>
        <div class="perm-row shaded"><div>Data Source</div><div>Role</div></div>
        <div class="perm-row"><div>All Data Sources</div><div>System Administrator</div></div>
      </div>
    </div>
    <div class="row item"><div><svg width="7" height="11" viewBox="0 0 7 11"><path d="M1 1l4.5 4.5L1 10" stroke="#363d63" stroke-width="2" fill="none"/></svg></div><div>Test</div><div>User</div><div>test.User</div><div>tim@kestreldata.net</div><div>Active</div><div class="actions"><span class="act"><svg width="12" height="12" viewBox="0 0 12 12"><path d="M1 11l1-3 6-6 2 2-6 6z" fill="#fff"/></svg></span><span class="act"><svg width="12" height="12" viewBox="0 0 12 12"><rect x="3" y="1" width="8" height="8" fill="#fff"/><path d="M1 3v8h8" stroke="#fff" stroke-width="1.4" fill="none"/></svg></span><span class="act del"><svg width="11" height="12" viewBox="0 0 11 12"><path d="M0 2h11M4 0h3" stroke="#fff" stroke-width="1.4"/><path d="M1.5 3h8l-.7 9H2.2z" fill="#fff"/></svg></span></div></div>
    <div class="row item"><div><svg width="7" height="11" viewBox="0 0 7 11"><path d="M1 1l4.5 4.5L1 10" stroke="#363d63" stroke-width="2" fill="none"/></svg></div><div>Test</div><div>User</div><div>test.User</div><div>tim@kestreldata.net</div><div>Active</div><div class="actions"><span class="act"><svg width="12" height="12" viewBox="0 0 12 12"><path d="M1 11l1-3 6-6 2 2-6 6z" fill="#fff"/></svg></span><span class="act"><svg width="12" height="12" viewBox="0 0 12 12"><rect x="3" y="1" width="8" height="8" fill="#fff"/><path d="M1 3v8h8" stroke="#fff" stroke-width="1.4" fill="none"/></svg></span><span class="act del"><svg width="11" height="12" viewBox="0 0 11 12"><path d="M0 2h11M4 0h3" stroke="#fff" stroke-width="1.4"/><path d="M1.5 3h8l-.7 9H2.2z" fill="#fff"/></svg></span></div></div>
    <div class="row item"><div><svg width="7" height="11" viewBox="0 0 7 11"><path d="M1 1l4.5 4.5L1 10" stroke="#363d63" stroke-width="2" fill="none"/></svg></div><div>Test</div><div>User</div><div>test.User</div><div>tim@kestreldata.net</div><div>Active</div><div class="actions"><span class="act"><svg width="12" height="12" viewBox="0 0 12 12"><path d="M1 11l1-3 6-6 2 2-6 6z" fill="#fff"/></svg></span><span class="act"><svg width="12" height="12" viewBox="0 0 12 12"><rect x="3" y="1" width="8" height="8" fill="#fff"/><path d="M1 3v8h8" stroke="#fff" stroke-width="1.4" fill="none"/></svg></span><span class="act del"><svg width="11" height="12" viewBox="0 0 11 12"><path d="M0 2h11M4 0h3" stroke="#fff" stroke-width="1.4"/><path d="M1.5 3h8l-.7 9H2.2z" fill="#fff"/></svg></span></div></div>
    <div class="row item"><div><svg width="7" height="11" viewBox="0 0 7 11"><path d="M1 1l4.5 4.5L1 10" stroke="#363d63" stroke-width="2" fill="none"/></svg></div><div>Test</div><div>User</div><div>test.User</div><div>tim@kestreldata.net</div><div>Active</div><div class="actions"><span class="act"><svg width="12" height="12" viewBox="0 0 12 12"><path d="M1 11l1-3 6-6 2 2-6 6z" fill="#fff"/></svg></span><span class="act"><svg width="12" height="12" viewBox="0 0 12 12"><rect x="3" y="1" width="8" height="8" fill="#fff"/><path d="M1 3v8h8" stroke="#fff" stroke-width="1.4" fill="none"/></svg></span><span class="act del"><svg width="11" height="12" viewBox="0 0 11 12"><path d="M0 2h11M4 0h3" stroke="#fff" stroke-width="1.4"/><path d="M1.5 3h8l-.7 9H2.2z" fill="#fff"/></svg></span></div></div>
    <div class="row item"><div><svg width="7" height="11" viewBox="0 0 7 11"><path d="M1 1l4.5 4.5L1 10" stroke="#363d63" stroke-width="2" fill="none"/></svg></div><div>Test</div><div>User</div><div>test.User</div><div>tim@kestreldata.net</div><div>Active</div><div class="actions"><span class="act"><svg width="12" height="12" viewBox="0 0 12 12"><path d="M1 11l1-3 6-6 2 2-6 6z" fill="#fff"/></svg></span><span class="act"><svg width="12" height="12" viewBox="0 0 12 12"><rect x="3" y="1" width="8" height="8" fill="#fff"/><path d="M1 3v8h8" stroke="#fff" stroke-width="1.4" fill="none"/></svg></span><span class="act del"><svg width="11" height="12" viewBox="0 0 11 12"><path d="M0 2h11M4 0h3" stroke="#fff" stroke-width="1.4"/><path d="M1.5 3h8l-.7 9H2.2z" fill="#fff"/></svg></span></div></div>
  </div>
  <nav class="pager">
    <span class="pg wide">Prev</span><span class="pg current">1</span><span class="pg">2</span><span class="pg">3</span><span class="pg">4</span><span class="pg">5</span><span class="pg">6</span><span class="pg">…</span><span class="pg">22</span><span class="pg wide">Next</span>
  </nav>
</main>

<footer class="footer">Copyright © 2018. All Rights Reserved - Privacy Policy</footer>
</body>
</html>
```